'The Hollow Bell of the Winter Harbor' novel: book cover design (inc back & side)

My novel is called "The Hollow Bell of the Winter Harbor" and the subtitle is "A defeated soldier battles the Yakuza"
The book's description is:
"In December 1945 Daiki Tanemura, an Northern Guard officer, returns to war torn Osaka. He is a rare survivor from the Philippines campaign. Japan is in a wretched state, flattened by intensive bombing. Starvation and homelessness are rampant. Branded a defeated soldier, survivors treat him as an outcast. Penniless, he sleeps rough.
Amidst the city’s ruins and chaos, Black Markets explode. Some traders hawk goods looted from military stock piles. Others sell contraband sourced from racketeers in the occupation authorities. Yakuza gangs control the Black Markets, bribing police and city officials who turn a blind eye.
Tanemura’s former Corporal runs a stall in the Oritani Black Market. Shaken down by the mob, he pleads for help. Can Tanemura help? Will Tanemura rediscover his once proud and invincible Samurai spirit?
The Hollow Bell of the Winter Harbor is a novel based on eye witness accounts and news reports.
Postwar Japan was a time when the weak were meat; the strong eat. "
The book design should apply for front, back and side. It will be an ePub and also printed version. The design should also work as a impactful thumbnail.
I need a designer who has interest or knowledge of Japan, where I live. Aspect ratio of 1.6 for the cover, size to 4500 pixels on the longest side.
I will supply the author's name later
Historical fiction readers; people interested in Japan & Japanese history; crime
- An impactful cover design that works on printed, e-pub and also Vendora thumbnail. The design must be for front, back and side
- (Impactful = attractive, high standout, intrigues reader to buy the book)
- I have attached some imagery of post war Japan, the era when the novel is set.
- Note: the hero of the story is the defeated solider, not the Yakuza
- stock image photos

```html
<!DOCTYPE html>
<html lang="en">
<head>
<meta charset="utf-8">
<title>The Hollow Bell of the Winter Harbor — Full Cover</title>
<link href="https://fonts.googleapis.com/css2?family=Montserrat:wght@400;500;700;800&display=swap" rel="stylesheet">
<style>
  :root {
    --paper: #ffffff;
    --ink: #111111;
    --crimson: #e0341a;
    --dusk-top: #8a9ab4;
    --dusk-mid: #3f6fb5;
    --dusk-low: #0e1f4a;
  }
  html, body {
    margin: 0;
    padding: 0;
    overflow: hidden;
    background: var(--paper);
  }
  .cover {
    position: relative;
    width: 1200px;
    height: 830px;
    background: var(--paper);
    overflow: hidden;
    font-family: "Montserrat", sans-serif;
    color: var(--ink);
  }

  /* Back cover */
  .back-blurb {
    position: absolute;
    left: 40px;
    top: 52px;
    width: 476px;
    font-size: 14.4px;
    line-height: 15.4px;
    font-weight: 400;
    text-align: justify;
  }
  .back-blurb p { margin: 0 0 15.4px; }
  .back-marks {
    position: absolute;
    left: 130px;
    top: 456px;
    display: flex;
    gap: 45px;
  }
  .blossom-mark {
    width: 58px;
    height: 58px;
    border-radius: 50%;
    background: var(--crimson);
  }

  /* Spine */
  .spine-author {
    position: absolute;
    left: 600px;
    top: 176px;
    transform: translate(-50%, -50%) rotate(-90deg);
    white-space: nowrap;
    font-size: 20px;
    font-weight: 500;
    letter-spacing: 12px;
    padding-left: 12px;
  }
  .spine-mark {
    position: absolute;
    left: 571px;
    top: 357px;
    width: 58px;
    height: 58px;
    border-radius: 50%;
    background: var(--crimson);
  }
  .spine-title {
    position: absolute;
    left: 600px;
    top: 620px;
    transform: translate(-50%, -50%) rotate(-90deg);
    white-space: nowrap;
    font-size: 14px;
    font-weight: 700;
    letter-spacing: 0.5px;
  }

  /* Front cover */
  .front-title {
    position: absolute;
    left: 640px;
    width: 580px;
    top: 28px;
    margin: 0;
    text-align: center;
    font-weight: 800;
    text-transform: uppercase;
  }
  .front-title .lead { display: block; font-size: 31px; line-height: 31px; }
  .front-title .main { display: block; font-size: 58px; line-height: 58px; margin-top: 2px; letter-spacing: 0.5px; }
  .front-title .tail { display: block; font-size: 35px; line-height: 35px; margin-top: 0; letter-spacing: 0.5px; }
  .front-subtitle {
    position: absolute;
    left: 640px;
    width: 580px;
    top: 170px;
    margin: 0;
    text-align: center;
    color: var(--crimson);
    font-size: 20.5px;
    font-weight: 700;
    letter-spacing: 2.2px;
  }
  .front-art {
    position: absolute;
    left: 684px;
    top: 210px;
    width: 474px;
    height: 620px;
  }
  .front-author {
    position: absolute;
    left: 670px;
    top: 760px;
    width: 514px;
    margin: 0;
    display: flex;
    justify-content: space-between;
    font-size: 44px;
    line-height: 48px;
    font-weight: 500;
  }
</style>
</head>
<body>
<main class="cover">

  <section class="back">
    <div class="back-blurb">
      <p>In December 1945 Daiki Tanemura, an Northern Guard officer, returns to war torn Osaka. He is a rare survivor from the Philippines campaign. Japan is in a wretched state, flattened by intensive bombing. Starvation and homelessness are rampant. Branded a defeated soldier, survivors treat him as an outcast. Penniless, he sleeps rough.</p>
      <p>Amidst the city’s ruins and chaos, Black Markets explode. Some traders hawk goods looted from military stock piles. Others sell contraband sourced from racketeers in the occupation authorities. Yakuza gangs control the Black Markets, bribing police and city officials who turn a blind eye.</p>
      <p>Tanemura’s former Corporal runs a stall in the Oritani Black Market. Shaken down by the mob, he pleads for help. Can Tanemura help? Will Tanemura rediscover his once proud and invincible Samurai spirit?</p>
      <p>The Hollow Bell of the Winter Harbor is a novel based on eye witness accounts and news reports.</p>
      <p>Postwar Japan was a time when the weak were meat; the strong eat.</p>
    </div>
    <div class="back-marks">
      <div class="blossom-mark" role="img" aria-label="Red plum blossom emblem"></div>
      <div class="blossom-mark" role="img" aria-label="Red plum blossom emblem"></div>
      <div class="blossom-mark" role="img" aria-label="Red plum blossom emblem"></div>
    </div>
  </section>

  <section class="spine">
    <div class="spine-author">AUTHOR NAME</div>
    <div class="spine-mark" role="img" aria-label="Red plum blossom emblem"></div>
    <div class="spine-title">THE HOLLOW BELL OF THE WINTER HARBOR</div>
  </section>

  <section class="front">
    <h1 class="front-title">
      <span class="lead">The</span>
      <span class="main">Hollow Bell</span>
      <span class="tail">of the Winter Harbor</span>
    </h1>
    <p class="front-subtitle">A defeated soldier battles the Yakuza</p>

    <svg class="front-art" viewBox="0 0 474 620" role="img"
         aria-label="Large red plum blossom behind a soldier's silhouette filled with a postwar street scene and cherry blossoms">
      <defs>
        <linearGradient id="dusk" x1="0" y1="0" x2="0" y2="1">
          <stop offset="0" stop-color="var(--dusk-top)"/>
          <stop offset="0.55" stop-color="var(--dusk-mid)"/>
          <stop offset="1" stop-color="var(--dusk-low)"/>
        </linearGradient>
      </defs>
      <circle cx="236" cy="216" r="214" fill="var(--crimson)"/>
      <rect x="68" y="34" width="360" height="586" rx="40" fill="url(#dusk)"/>
    </svg>

    <p class="front-author" aria-label="AUTHOR NAME">
      <span>A</span><span>U</span><span>T</span><span>H</span><span>O</span><span>R</span><span></span><span>N</span><span>A</span><span>M</span><span>E</span>
    </p>
  </section>

</main>
</body>
</html>
```